Sticker Design

I need a unique logo for a CIRCULAR sticker for musical artist, Crondel Vaux. I have attached two styles the artist prefers. The design should be circular. It should feature prominently "Crondel Vaux" and have his website smaller at the bottom "www.crondelvaux.net." The design should have a black or dark background. The artist is interested in seeing his name in a neon style (pink). But he would consider something else original, in line with, but not exactly the same as, the other reference supplied. This is a guaranteed project. Thank you for your talents.

```html
<!DOCTYPE html>
<html lang="en">
<head>
<meta charset="UTF-8">
<title>Crondel Vaux — Sticker</title>
<link rel="stylesheet" href="https://fonts.googleapis.com/css2?family=Oswald:wght@300;400&display=swap">
<style>
  :root {
    --page: #ffffff;
    --sticker-dark: #0b0b0b;
    --sticker-mid: #2a2a2a;
    --sticker-soft: #3d3d3d;
    --neon: #ff1f9a;
    --neon-deep: #c0106f;
    --neon-soft: #e24fa6;
    --white: #f4f4f4;
  }
  html, body {
    margin: 0;
    width: 1200px;
    height: 1200px;
    overflow: hidden;
    background: var(--page);
  }
  .canvas {
    position: relative;
    width: 1200px;
    height: 1200px;
  }
  .sticker {
    position: absolute;
    left: 134px;
    top: 143px;
    width: 920px;
    height: 920px;
    border-radius: 50%;
    overflow: hidden;
    background: var(--sticker-dark);
  }
  .sticker-portrait {
    position: absolute;
    inset: 0;
    width: 100%;
    height: 100%;
  }
  .name-small,
  .name-neon,
  .name-ghost,
  .website {
    position: absolute;
    margin: 0;
    font-family: "Oswald", "Arial Narrow", sans-serif;
    text-transform: uppercase;
    white-space: nowrap;
    line-height: 1;
  }
  .name-small {
    left: 335px;
    top: 528px;
    font-size: 54px;
    font-weight: 300;
    color: var(--neon-soft);
    opacity: 0.85;
    letter-spacing: 1px;
  }
  .name-ghost {
    left: 74px;
    top: 572px;
    font-size: 108px;
    font-weight: 400;
    color: var(--neon-deep);
    opacity: 0.55;
    filter: blur(5px);
  }
  .name-neon {
    left: 84px;
    top: 588px;
    font-size: 108px;
    font-weight: 400;
    color: var(--neon);
    text-shadow:
      0 0 6px var(--neon),
      0 0 18px var(--neon),
      0 0 36px var(--neon-deep);
  }
  .website {
    left: 312px;
    top: 722px;
    font-size: 54px;
    font-weight: 300;
    color: var(--white);
  }
</style>
</head>
<body>
<main class="canvas">
  <section class="sticker">
    <svg class="sticker-portrait" viewBox="0 0 920 920" role="img" aria-label="Dark black-and-white portrait of the artist filling the circular sticker">
      <defs>
        <radialGradient id="portraitTone" cx="52%" cy="35%" r="65%">
          <stop offset="0" stop-color="var(--sticker-soft)"/>
          <stop offset="0.5" stop-color="var(--sticker-mid)"/>
          <stop offset="1" stop-color="var(--sticker-dark)"/>
        </radialGradient>
      </defs>
      <rect width="920" height="920" fill="url(#portraitTone)"/>
    </svg>
    <p class="name-small">Crondel Vaux</p>
    <p class="name-ghost" aria-hidden="true">Crondel Vaux</p>
    <h1 class="name-neon">Crondel Vaux</h1>
    <p class="website">www.crondelvaux.net</p>
  </section>
</main>
</body>
</html>
```